Delia Morvan
exclusive handcrafted jewelry
Simple
delmorvan@quillbox.net
deliamorvandesign.net
business card should be shaded black like uploaded logo.
I also like the royal blue option !
I have no idea what is on that file since I can not open it . I hope it is my logo in blue or shaded black.

```html
<!DOCTYPE html>
<html lang="en">
<head>
<meta charset="utf-8">
<title>Delia Morvan – Business Card</title>
<link rel="stylesheet" href="https://fonts.googleapis.com/css2?family=Arvo:wght@400;700&family=Courier+Prime&display=swap">
<style>
  :root {
    --backdrop: #e9e6e1;
    --card-white: #fbfbfb;
    --card-grey: #d9d9d9;
    --royal-blue: #1d6fcb;
    --royal-blue-light: #3d9ae8;
    --ink-black: #121212;
    --ink-white: #ffffff;
    --ink-dark-blue: #0c2d55;
  }
  html, body {
    margin: 0;
    padding: 0;
    overflow: hidden;
  }
  body {
    width: 1200px;
    height: 852px;
    background: var(--backdrop);
    display: flex;
    align-items: center;
    justify-content: center;
    gap: 60px;
  }
  .card {
    position: relative;
    width: 540px;
    height: 310px;
    border-radius: 22px;
    overflow: hidden;
    background: linear-gradient(180deg, var(--card-white) 0%, var(--card-grey) 100%);
    box-shadow: 0 6px 18px rgba(0, 0, 0, 0.18);
  }
  .card-band {
    position: absolute;
    inset: 0;
    width: 100%;
    height: 100%;
  }
  .brand-mark {
    position: absolute;
    top: 58px;
    left: 150px;
    display: flex;
    align-items: center;
    gap: 12px;
    font-family: "Arvo", serif;
    font-weight: 400;
    font-size: 34px;
    color: var(--ink-black);
  }
  .brand-dot {
    width: 22px;
    height: 22px;
    border-radius: 50%;
    background: var(--ink-black);
  }
  .holder {
    position: absolute;
    right: 38px;
    top: 178px;
    text-align: right;
    color: var(--ink-white);
  }
  .holder-name {
    margin: 0;
    font-family: "Arvo", serif;
    font-weight: 700;
    font-size: 32px;
    letter-spacing: -0.5px;
  }
  .holder-phone {
    margin: 6px 0 0;
    font-family: "Courier Prime", monospace;
    font-size: 19px;
  }
  .contact-lines {
    position: absolute;
    left: 36px;
    top: 168px;
    margin: 0;
    padding: 0;
    list-style: none;
    font-family: "Courier Prime", monospace;
    font-size: 19px;
    line-height: 1.5;
    color: var(--ink-dark-blue);
  }
</style>
</head>
<body>

  <section class="card card-front">
    <svg class="card-band" viewBox="0 0 540 310" preserveAspectRatio="none" aria-hidden="true">
      <defs>
        <linearGradient id="bandFront" x1="0" y1="0" x2="1" y2="0">
          <stop offset="0" stop-color="var(--royal-blue)"/>
          <stop offset="0.55" stop-color="var(--royal-blue-light)"/>
          <stop offset="1" stop-color="var(--royal-blue)"/>
        </linearGradient>
      </defs>
      <path d="M0 120 C 140 60, 300 150, 540 70 L 540 262 C 380 262, 160 282, 0 292 Z" fill="url(#bandFront)"/>
    </svg>
    <div class="brand-mark">
      <span class="brand-dot"></span>
      <span class="brand-name">Delia Morvan</span>
    </div>
    <div class="holder">
      <p class="holder-name">Delia Morvan</p>
      <p class="holder-phone">555-210-3876</p>
    </div>
  </section>

  <section class="card card-back">
    <svg class="card-band" viewBox="0 0 540 310" preserveAspectRatio="none" aria-hidden="true">
      <defs>
        <linearGradient id="bandBack" x1="0" y1="0" x2="1" y2="0">
          <stop offset="0" stop-color="var(--royal-blue)"/>
          <stop offset="0.55" stop-color="var(--royal-blue-light)"/>
          <stop offset="1" stop-color="var(--royal-blue)"/>
        </linearGradient>
      </defs>
      <path d="M0 70 C 200 40, 360 120, 540 60 L 540 262 C 380 262, 160 282, 0 292 Z" fill="url(#bandBack)"/>
    </svg>
    <ul class="contact-lines">
      <li class="contact-web">deliamorvandesign.net</li>
      <li class="contact-email">delmorvan@quillbox.net</li>
    </ul>
  </section>

</body>
</html>
```